Text only wordpress site to capture emails

Refer to inspiration upload for list of sites that will be useful for you.

We need a site that will be used to capture emails from clients that follow us on social media. The site will be all text, pretty simple. I have a couple of text sites that I like and we can use them for an example.

Menu section will have home, archive, about.
Footer will have © and Website Privacy Policy | Legal and Policies
There will be some text on the home page and an email capture.

This site will be all text no pictures.

I discuss Cubicle Capers so the text portions will have some questions and answers on this and then prompt for the visitor to subscribe to my email list.

The only purpose of the site is to build an email list from existing social media followers so the site will be pretty simple in and of itself.

• Text only, similar Q&A to uploaded pics.

I will use a template from letter pinecone dotcom for email capture.

I like the simple couriernew font family that is on both sites supplied in the uploads.
• If you use any color it needs to be very minimal.

```html
<!DOCTYPE html>
<html lang="en">
<head>
<meta charset="utf-8">
<title>Cubicle Capers</title>
<link href="https://fonts.googleapis.com/css2?family=Courier+Prime&family=Original+Surfer&display=swap" rel="stylesheet">
<style>
  :root {
    --ink: #111111;
    --muted: #444444;
    --rule: #8a2433;
    --field-border: #c9c9c9;
    --button-bg: #e4e4e4;
    --chip-border: #dddddd;
    --paper: #ffffff;
  }
  * { box-sizing: border-box; margin: 0; padding: 0; }
  html, body { width: 1200px; height: 985px; overflow: hidden; background: var(--paper); color: var(--ink); }
  body { font-family: "Courier Prime", "Courier New", monospace; position: relative; }
  .display { font-family: "Original Surfer", cursive; font-weight: 400; white-space: nowrap; }
  .narrow { display: inline-block; transform-origin: left top; }

  .site-header {
    position: absolute; left: 141px; top: 0; width: 919px; height: 84px;
    border-bottom: 1px solid var(--rule);
  }
  .site-title { position: absolute; left: 0; top: 22px; font-size: 35px; line-height: 46px; }
  .site-title .narrow { transform: scaleX(0.79); }
  .main-nav { position: absolute; top: 28px; left: 0; width: 919px; }
  .main-nav a { position: absolute; font-size: 20px; line-height: 26px; color: var(--ink); text-decoration: none; }
  .main-nav .narrow { transform: scaleX(0.76); }
  .nav-home { left: 652px; }
  .nav-archive { left: 744px; }
  .nav-about { left: 852px; }

  .signup { position: absolute; left: 141px; top: 170px; width: 353px; }
  .signup-heading { font-size: 34px; line-height: 36px; }
  .signup-heading .narrow { transform: scaleX(0.72); }
  .signup-intro { margin-top: 16px; padding-left: 2px; font-size: 14px; line-height: 20px; color: var(--muted); }
  .email-field {
    display: block; margin-top: 17px; width: 353px; height: 39px;
    border: 1px solid var(--field-border); background: var(--paper);
    padding: 0 9px; font: 15px "Courier Prime", "Courier New", monospace; color: var(--muted);
  }
  .email-field::placeholder { color: var(--muted); }
  .subscribe-button {
    display: block; margin-top: 14px; width: 141px; height: 39px;
    border: 0; border-radius: 3px; background: var(--button-bg);
    font: 14px "Courier Prime", "Courier New", monospace; color: var(--ink);
  }

  .faq { position: absolute; left: 559px; top: 164px; width: 495px; }
  .faq-title { font-size: 18px; line-height: 22px; }
  .faq-title .narrow { transform: scaleX(0.87); }
  .faq-lede { margin-top: 7px; font-size: 12.7px; line-height: 18px; color: var(--muted); }
  .qa { position: absolute; left: 0; width: 495px; }
  .qa-question { font-size: 15.5px; line-height: 20px; }
  .qa-question .narrow { transform: scaleX(0.87); }
  .qa-answer { margin-top: 2px; display: flex; font-size: 12.7px; line-height: 17.6px; color: var(--muted); }
  .qa-answer .label { flex: 0 0 16px; }
  .qa-answer .text { width: 472px; }

  .site-footer {
    position: absolute; left: 141px; top: 916px; width: 919px; height: 69px;
    border-top: 1px solid var(--rule);
  }
  .copyright { position: absolute; left: 0; top: 20px; font-size: 13px; color: var(--muted); white-space: nowrap; }
  .social { position: absolute; right: 0; top: 28px; display: flex; gap: 8px; }
  .social a {
    height: 32px; padding: 0 8px; border: 1px solid var(--chip-border); border-radius: 3px;
    display: flex; align-items: center; font-size: 11px; color: var(--ink); text-decoration: none;
  }
</style>
</head>
<body>
  <header class="site-header">
    <div class="site-title display"><span class="narrow">Cubicle Capers</span></div>
    <nav class="main-nav display">
      <a class="nav-home" href="#"><span class="narrow">Home</span></a>
      <a class="nav-archive" href="#"><span class="narrow">Archive</span></a>
      <a class="nav-about" href="#"><span class="narrow">About Us</span></a>
    </nav>
  </header>

  <section class="signup">
    <h1 class="signup-heading display"><span class="narrow">Scurrilous Gossip.<br>Scandalous Politics.Otters.</span></h1>
    <p class="signup-intro">Sign up for the Lorem im dolor sit amet, consectetuer adipiscing elit.</p>
    <input class="email-field" type="email" placeholder="Email Address">
    <button class="subscribe-button" type="button">Subscribe</button>
  </section>

  <section class="faq">
    <h2 class="faq-title display"><span class="narrow">About Cubicle Capers</span></h2>
    <p class="faq-lede">Lorem ipsum dolor sit amet, consectetuer adipiscing elit....</p>

    <div class="qa" style="top:80px">
      <h3 class="qa-question display"><span class="narrow">Q:Ut wisi enim ad minim veniam, quis nostrud exerci?</span></h3>
      <p class="qa-answer"><span class="label">A:</span><span class="text">Lorem ipsum dolor sit amet, consectetuer adipiscing elit, sed diam nonummy nibh euismod tincidunt ut laoreet dolorena aliquam erat volutpat. Ut wisi enim ad minim veniam quis.</span></p>
    </div>
    <div class="qa" style="top:191px">
      <h3 class="qa-question display"><span class="narrow">Q:Sed diam nonummy nibh euismod tincidunt?</span></h3>
      <p class="qa-answer"><span class="label">A:</span><span class="text">Lorem ipsum dolor sit amet, consectetuer adipiscing elit, sed diam nonummy nibh euismod tincidunt ut laoreet dolorena aliquam erat volutpat. Ut wisi enim ad minim veniam quis.</span></p>
    </div>
    <div class="qa" style="top:304px">
      <h3 class="qa-question display"><span class="narrow">Q:Duis autem vel eum iriure dolor in hendrerit in vulputate?</span></h3>
      <p class="qa-answer"><span class="label">A:</span><span class="text">Lorem ipsum dolor sit amet, consectetuer adipiscing elit, sed diam nonummy nibh euismod tincidunt ut laoreet.</span></p>
    </div>
    <div class="qa" style="top:399px">
      <h3 class="qa-question display"><span class="narrow">Q:Sed diam nonummy nibh euismod tincidunt?</span></h3>
      <p class="qa-answer"><span class="label">A:</span><span class="text">Lorem ipsum dolor sit amet, consectetuer adipiscing elit, sed diam nonummy nibh euismod tincidunt ut laoreet dolorena aliquam erat volutpat. Ut wisi enim ad minim veniam quis.</span></p>
    </div>
    <div class="qa" style="top:512px">
      <h3 class="qa-question display"><span class="narrow">Q:Ut wisi enim ad minim veniam, quis nostrud exerci?</span></h3>
      <p class="qa-answer"><span class="label">A:</span><span class="text">Lorem ipsum dolor sit amet, consectetuer adipiscing elit, sed diam nonummy nibh euismod tincidunt ut laoreet dolorena aliquam erat volutpat. Ut wisi enim ad minim veniam quis.</span></p>
    </div>
    <div class="qa" style="top:625px">
      <h3 class="qa-question display"><span class="narrow">Q:Duis autem vel eum iriure dolor in hendrerit in vulputate?</span></h3>
      <p class="qa-answer"><span class="label">A:</span><span class="text">Lorem ipsum dolor sit amet, consectetuer adipiscing elit, sed diam nonummy nibh euismod tincidunt ut laoreet.</span></p>
    </div>
  </section>

  <footer class="site-footer">
    <p class="copyright">Copyright © 2021 Cubicle Capers. All Right Reserved. Privacy Policy | Legal and Policies</p>
    <nav class="social">
      <a href="#">Palbook</a>
      <a href="#">Glimpse</a>
      <a href="#">Chirper</a>
    </nav>
  </footer>
</body>
</html>
```